Coastwell Keys Agency Guarantee

We need a flyer to promote a Sydney based property management agency.
We specialise in Property Management on the Northern Beaches of Sydney. A small boutique agency that prides itself on high quality customer service and the lowest fees.
We would like this flyer to promote our listed features in the document provided and focus on our money back guarantee.
The flyer must:
- be designed to match our website www.coastwellkeysagency.com.au
- Contain our logo and contact details
- Use the attached photoshop template for bleed, sizing and fold lines
- final files must include a print ready PDF and fully editable PSD (photoshop) file with included fonts.
Attached are the following files:
Contact details are:
Name: Tom Farrow
Tel: 0491 527 068
email: tom@coastwellkeysagency.com.au
Office: Level 2, 17 Tennerby Rd, Marlow Heights NSW 2188
Web: www.coastwellkeysagency.com.au
Target Market(s)
35-75yo Male and Females that own investment properties on Sydney's Norther Beaches
Industry/Entity Type
Real Estate
Requirements
Must have
- The flyer must:
- - Be double sided and colour
- - be designed to match our website www.coastwellkeysagency.com.au
- - Contain our logo and contact details
- - Use the attached photoshop template for bleed, sizing and fold lines
- - final files must include a print ready PDF and fully editable PSD (photoshop) file with included fonts.
Nice to have
- A Money back guarantee "stamp"

```html
<!DOCTYPE html>
<html lang="en">
<head>
<meta charset="utf-8">
<title>Coastwell Keys Agency – Guarantee Flyer</title>
<link href="https://fonts.googleapis.com/css2?family=Montserrat:wght@400;500;600;700&display=swap" rel="stylesheet">
<style>
  :root {
    --ink: #1e1e1e;
    --panel-dark: #101a1c;
    --panel-dark-2: #1b2c30;
    --teal: #2a7e8c;
    --teal-bright: #2b8fa0;
    --paper: #ffffff;
    --stage: #dcdcdc;
    --gold: #c9a12f;
    --gold-dark: #8a6a12;
  }
  * { box-sizing: border-box; margin: 0; padding: 0; }
  html, body { width: 1200px; height: 800px; overflow: hidden; }
  body {
    background: var(--stage);
    font-family: "Montserrat", sans-serif;
    color: var(--ink);
    display: flex; align-items: center; justify-content: center;
  }
  .brochure { width: 1140px; height: 760px; display: flex; background: var(--paper); }
  .panel { position: relative; width: 380px; height: 760px; overflow: hidden; }
  .panel svg.shapes { position: absolute; inset: 0; }

  .panel-footer {
    position: absolute; left: 0; right: 0; bottom: 0; height: 70px;
    background: var(--paper);
    border-bottom: 7px solid var(--teal);
    display: flex; align-items: center; justify-content: center;
    font-size: 15px; font-weight: 500; letter-spacing: 0.5px;
  }

  /* Guarantee panel */
  .guarantee { background: linear-gradient(160deg, var(--panel-dark-2), var(--panel-dark) 60%); }
  .guarantee-frame {
    position: absolute; left: 16px; right: 16px; top: 18px; height: 656px;
    border: 1.5px solid rgba(255,255,255,0.8);
  }
  .guarantee-title {
    position: absolute; top: 30px; left: 30px; right: 30px;
    display: flex; align-items: center; gap: 12px;
    color: var(--paper); font-size: 22px; font-weight: 600;
  }
  .guarantee-title::before, .guarantee-title::after {
    content: ""; flex: 1; height: 1.5px; background: rgba(255,255,255,0.8);
  }
  .guarantee-copy {
    position: absolute; top: 80px; left: 32px; right: 30px;
    color: var(--paper); font-size: 12.5px; line-height: 1.32; letter-spacing: 1px;
  }
  .guarantee-copy p + p { margin-top: 10px; }
  .guarantee-photo {
    position: absolute; left: 40px; right: 40px; top: 510px; height: 100px;
    border: 3px solid var(--paper);
    background: linear-gradient(180deg, #3e8ec2 0%, #8cc1dd 45%, #3f5a3a 70%, #2b3d2a 100%);
  }
  .guarantee-seal {
    position: absolute; left: 268px; top: 482px; width: 70px; height: 70px;
    border-radius: 50%;
    background: radial-gradient(circle, #e8c451 0 55%, var(--gold) 56% 78%, var(--gold-dark) 79%);
    border: 3px solid #1a1a1a;
  }
  .guarantee-note {
    position: absolute; left: 40px; right: 36px; top: 622px;
    color: var(--paper); font-size: 9.5px; line-height: 1.35; letter-spacing: 0.6px;
  }

  /* Name stand-in */
  .brand-name {
    font-weight: 600; color: var(--ink); letter-spacing: 0.3px; white-space: nowrap;
    display: flex; align-items: center; gap: 8px;
  }
  .brand-name::before { content: ""; width: 12px; height: 12px; border-radius: 50%; background: var(--teal); }

  /* Contact panel */
  .contact .brand-name { position: absolute; top: 412px; left: 0; right: 0; justify-content: center; font-size: 19px; }
  .contact-details { position: absolute; top: 492px; left: 0; right: 0; text-align: center; color: var(--paper); }
  .contact-name { font-size: 18px; font-weight: 700; margin-bottom: 14px; }
  .contact-line { font-size: 14px; letter-spacing: 0.5px; margin-bottom: 12px; line-height: 1.3; }
  .contact-line svg { display: block; margin: 0 auto 4px; }

  /* Cover panel */
  .cover .brand-name { position: absolute; top: 36px; left: 0; right: 0; justify-content: center; font-size: 19px; }
  .cover-headline {
    position: absolute; top: 500px; left: 30px; right: 30px;
    text-transform: uppercase; color: var(--paper); letter-spacing: 2px; line-height: 1.15;
  }
  .cover-headline span { display: block; font-weight: 500; }
  .cover-headline .line-1 { font-size: 40px; }
  .cover-headline .line-2 { font-size: 29px; }
  .cover-headline .line-3 { font-size: 29px; color: var(--teal-bright); }
</style>
</head>
<body>
<main class="brochure">

  <section class="panel guarantee">
    <div class="guarantee-frame"></div>
    <h2 class="guarantee-title">Our Guarantee:</h2>
    <div class="guarantee-copy">
      <p>At Coastwell Keys Agency we are the Risk Reduction Specialists! Our team will work with you to ensure you're receiving the highest possible return on your investment property. The entire department are heavily focused on maximising your income and optimising capital growth on your investment property.</p>
      <p>We understand when you are selecting a new managing agent it can be a very stressful process for many landlords as you don't know if they are going to deliver on their promises.</p>
      <p>At Coastwell Keys Agency we understand promises can be easily broken and the good news is we GUARANTEE our service.</p>
      <p>If during the first 3 months you are not satisfied with our level of service we promise to you. We are prepared to refund the first 3 months and will give 100% money back on your management fees*.</p>
    </div>
    <div class="guarantee-photo" role="img" aria-label="Photo of a modern two-storey home framed by garden greenery under a blue sky"></div>
    <div class="guarantee-seal" role="img" aria-label="Gold money back guarantee seal"></div>
    <p class="guarantee-note">*Only applies to management fees. Coastwell Keys Agency must be notified in writing within the 3 month service guarantee period.</p>
    <footer class="panel-footer">www.coastwellkeysagency.com.au</footer>
  </section>

  <section class="panel contact">
    <svg class="shapes" width="380" height="760" viewBox="0 0 380 760">
      <defs>
        <linearGradient id="estate-tones" x1="0" y1="0" x2="0" y2="1">
          <stop offset="0" stop-color="#4aa3d4"/>
          <stop offset="0.3" stop-color="#a9d3e8"/>
          <stop offset="0.45" stop-color="#3b3f42"/>
          <stop offset="0.7" stop-color="#4f7a3a"/>
          <stop offset="1" stop-color="#9a9d96"/>
        </linearGradient>
      </defs>
      <path role="img" aria-label="Photo of terraced modern townhouses with landscaped garden stairs" d="M0 0H380V372Q250 420 0 398Z" fill="url(#estate-tones)"/>
      <path d="M0 478Q200 438 380 458V690H0Z" fill="var(--teal)"/>
    </svg>
    <div class="brand-name">Coastwell Keys Agency</div>
    <div class="contact-details">
      <div class="contact-name">Tom Farrow</div>
      <div class="contact-line">
        <svg width="14" height="12" viewBox="0 0 14 12"><path d="M1 4Q7 -1 13 4L11 6L9 4.5V3.5Q7 2.8 5 3.5V4.5L3 6Z M3.5 6.5H10.5L12 11H2Z" fill="#fff"/></svg>
        0491 527 068
      </div>
      <div class="contact-line">
        <svg width="14" height="10" viewBox="0 0 14 10"><rect x="0.5" y="0.5" width="13" height="9" fill="#fff"/><path d="M0.5 0.5L7 5.5L13.5 0.5" stroke="#2a7e8c" fill="none"/></svg>
        tom@coastwellkeysagency.com.au
      </div>
      <div class="contact-line">
        <svg width="10" height="14" viewBox="0 0 10 14"><path d="M5 0A5 5 0 0 1 10 5C10 9 5 14 5 14S0 9 0 5A5 5 0 0 1 5 0Z" fill="#fff"/><circle cx="5" cy="5" r="2" fill="#2a7e8c"/></svg>
        Level 2, 17 Tennerby Rd,<br>Marlow Heights NSW 2188
      </div>
    </div>
    <footer class="panel-footer">www.coastwellkeysagency.com.au</footer>
  </section>

  <section class="panel cover">
    <svg class="shapes" width="380" height="760" viewBox="0 0 380 760">
      <defs>
        <linearGradient id="cover-tones" x1="0" y1="0" x2="0" y2="1">
          <stop offset="0" stop-color="#5ab0dc"/>
          <stop offset="0.3" stop-color="#c6e2ef"/>
          <stop offset="0.55" stop-color="#5f8a4a"/>
          <stop offset="1" stop-color="#a6aaa3"/>
        </linearGradient>
      </defs>
      <path role="img" aria-label="Photo of the agent standing with arms folded in front of townhouses and gardens" d="M0 0H380V420L0 470Z" fill="url(#cover-tones)"/>
      <path d="M0 470Q200 450 380 405V690H0Z" fill="#0b0b0b"/>
    </svg>
    <div class="brand-name">Coastwell Keys Agency</div>
    <h1 class="cover-headline">
      <span class="line-1">Property</span>
      <span class="line-2">Management</span>
      <span class="line-3">Done Right!</span>
    </h1>
    <footer class="panel-footer">www.coastwellkeysagency.com.au</footer>
  </section>

</main>
</body>
</html>
```